Bref créative
Brightwave IT Business cards
Professional
Kenneth Darrow
Chief Information Officer
248 Maple Hollow Rd
KDarrow@BrightwaveIT.example
www.brightwaveit.example
IT managed services
Managed backups
Web Hosting
Email Hosting
Spam Filtering
Networking
Structured Cabling
Project Planning
Colocation Services

```html
<!DOCTYPE html>
<html lang="en">
<head>
<meta charset="utf-8">
<title>Brightwave IT – Business Cards</title>
<link href="https://fonts.googleapis.com/css2?family=Questrial&display=swap" rel="stylesheet">
<style>
  :root {
    --stage: #4a2417;
    --navy: #14468c;
    --blue: #1f64b8;
    --sky: #5fa3e0;
    --mist: #d6e7f6;
    --paper: #ffffff;
    --ink: #1a2a40;
    --label: #f2ece8;
  }
  * { margin: 0; padding: 0; box-sizing: border-box; }
  html, body {
    width: 1200px; height: 874px; overflow: hidden;
    background: var(--stage);
    font-family: "Questrial", "Century Gothic", sans-serif;
  }
  .canvas { position: relative; width: 1200px; height: 874px; }

  .card {
    position: absolute; width: 540px; height: 310px;
    background: var(--paper); overflow: hidden;
    box-shadow: 0 10px 30px rgba(0,0,0,.45);
  }
  .card--front { left: 40px; top: 250px; }
  .card--back { left: 620px; top: 250px; }
  .card__art { position: absolute; inset: 0; }

  .caption {
    position: absolute; top: 584px; color: var(--label);
    font-size: 18px; letter-spacing: .5px;
  }
  .caption--front { left: 40px; }
  .caption--back { left: 620px; }

  .brand {
    position: absolute; left: 150px; top: 26px;
    display: flex; align-items: center; gap: 10px;
  }
  .brand__dot { width: 34px; height: 34px; border-radius: 50%; background: var(--blue); }
  .brand__name { font-size: 32px; color: var(--navy); letter-spacing: 1px; }

  .identity {
    position: absolute; left: 4px; bottom: 96px;
    transform: rotate(-90deg); transform-origin: left bottom;
    color: var(--paper); white-space: nowrap; translate: 40px 0;
  }
  .identity__name { font-size: 20px; font-weight: 700; letter-spacing: .5px; }
  .identity__title { font-size: 12px; margin-top: 1px; }

  .contact {
    position: absolute; left: 70px; top: 226px; width: 262px;
    color: var(--paper); font-size: 11.5px; line-height: 16px;
    display: grid; grid-template-columns: 52px 12px auto;
    white-space: nowrap;
  }
  .contact dt { font-weight: 700; }

  .services { position: absolute; left: 346px; top: 124px; width: 194px; }
  .services__head {
    background: linear-gradient(90deg, var(--blue), var(--sky));
    color: var(--paper); font-size: 13px; padding: 2px 10px; height: 19px;
  }
  .services__list { list-style: none; padding: 6px 0 0 10px; }
  .services__list li {
    font-size: 11.5px; color: var(--ink); line-height: 15.5px;
    display: flex; align-items: center; gap: 7px; white-space: nowrap;
  }
  .services__list li::before {
    content: ""; flex: none; width: 8px; height: 8px; border-radius: 50%;
    background: var(--blue); box-shadow: inset -1px -1px 0 var(--navy);
  }

  .back-mark {
    position: absolute; left: 22px; top: 34px;
    transform: rotate(90deg); transform-origin: left top; translate: 20px 0;
    color: rgba(255,255,255,.75); font-size: 22px; letter-spacing: 1px; white-space: nowrap;
  }
</style>
</head>
<body>
<main class="canvas">

  <section class="card card--front" aria-label="Business card front">
    <svg class="card__art" viewBox="0 0 540 310" preserveAspectRatio="none" aria-hidden="true">
      <defs>
        <linearGradient id="front-paper" x1="0" y1="1" x2="1" y2="0">
          <stop offset="0" stop-color="#ffffff"/>
          <stop offset=".55" stop-color="#eaf3fb"/>
          <stop offset="1" stop-color="#c4ddf3"/>
        </linearGradient>
        <linearGradient id="front-band" x1="0" y1="0" x2="1" y2="0">
          <stop offset="0" stop-color="#14468c"/>
          <stop offset=".45" stop-color="#2f79c8"/>
          <stop offset="1" stop-color="#9cc8ee" stop-opacity=".2"/>
        </linearGradient>
        <linearGradient id="front-edge" x1="0" y1="0" x2="0" y2="1">
          <stop offset="0" stop-color="#2a6fc0"/>
          <stop offset="1" stop-color="#14468c"/>
        </linearGradient>
      </defs>
      <rect width="540" height="310" fill="url(#front-paper)"/>
      <path d="M0 205 C160 190 300 205 540 250 L540 310 L0 310 Z" fill="url(#front-band)"/>
      <path d="M0 0 L58 0 C50 80 52 160 62 215 L0 215 Z" fill="url(#front-edge)"/>
      <path d="M58 0 C50 80 52 160 62 215" fill="none" stroke="#ffffff" stroke-opacity=".5" stroke-width="1.5"/>
      <path d="M0 212 C170 196 310 212 540 256" fill="none" stroke="#ffffff" stroke-opacity=".5" stroke-width="1.2"/>
    </svg>

    <div class="brand">
      <span class="brand__dot"></span>
      <span class="brand__name">Brightwave IT</span>
    </div>

    <div class="identity">
      <div class="identity__name">Kenneth Darrow</div>
      <div class="identity__title">Chief Information Officer</div>
    </div>

    <section class="services">
      <div class="services__head">Services</div>
      <ul class="services__list">
        <li>IT managed services</li>
        <li>Managed backups</li>
        <li>Web Hosting</li>
        <li>Email Hosting</li>
        <li>Spam Filtering</li>
        <li>Networking</li>
        <li>Structured Cabling</li>
        <li>Project Planning</li>
        <li>Colocation Services</li>
      </ul>
    </section>

    <dl class="contact">
      <dt>Address</dt><dd>:</dd><dd>248 Maple Hollow Rd</dd>
      <dt>Phone</dt><dd>:</dd><dd>555-014-2290</dd>
      <dt>Email</dt><dd>:</dd><dd>KDarrow@BrightwaveIT.example</dd>
      <dt>Web</dt><dd>:</dd><dd>www.brightwaveit.example</dd>
    </dl>
  </section>

  <section class="card card--back" aria-label="Business card back">
    <svg class="card__art" viewBox="0 0 540 310" preserveAspectRatio="none" aria-hidden="true">
      <defs>
        <linearGradient id="back-paper" x1="0" y1="1" x2="1" y2="0">
          <stop offset="0" stop-color="#ffffff"/>
          <stop offset="1" stop-color="#dfeaf6"/>
        </linearGradient>
        <linearGradient id="back-band" x1="0" y1="0" x2="1" y2="1">
          <stop offset="0" stop-color="#2a6fc0"/>
          <stop offset="1" stop-color="#14468c"/>
        </linearGradient>
      </defs>
      <rect width="540" height="310" fill="url(#back-paper)"/>
      <path d="M0 0 L40 0 C50 110 90 220 200 310 L0 310 Z" fill="url(#back-band)"/>
      <path d="M40 0 C50 110 90 220 200 310" fill="none" stroke="#ffffff" stroke-opacity=".6" stroke-width="1.5"/>
      <path d="M0 240 C150 220 330 250 540 300" fill="none" stroke="#c9dcef" stroke-width="1"/>
    </svg>
    <div class="back-mark">Brightwave IT</div>
  </section>

  <p class="caption caption--front">FRONT DESIGN</p>
  <p class="caption caption--back">BACK DESIGN</p>
</main>
</body>
</html>
```